Biz technology consulting firm like a global company (better than Corvantis, etc)

Check word document high level requirements, a_design_webpage_content attached providing more details for content and message to convey to potential customers..  Create a crisp, clear and engaging business consulting website design that allows the user to understand the value that Brimquarta can deliver to their company.  We focus on innovation, simplification, creative solutions, digital transformations ERP, CRM, Analytics, project management, making IT simple and coaching enterprises how to align and implement technologies to support business strategy and goals. Whether a startup or a global billion dollar firm, we increase EBITDA through innovation and digital transformation.  

I desire to have sections that highlight each of the core areas such as: (**Please see  brimquarta.example and the design word document that is attached below for core areas of focus**)

Feel free to go to Brimquarta.example and review the basic categories to understand at a very high level the categories that are key.

Help me create a brand and website that engages startups, Private Equity firms seeking carve-out, integration experience and large corporate enterprises searching to convert to data driven and customer focused enterprises.  
Hero section with a tagline that emphasizes the company's focus on Walking UP bolder.  We help you visualize outcomes with a positive and collaborative solution driven mindset.  When you look at life through a different "positive" lens, you can convert all problems to opportunities.  Align your IT team with your business goals and you quickly realize the value of all processes and technology deployed in your enterprise; increasing EBITDA, morale, and long term success.

We evaluate your current state, create a custom roadmap for alignment, coach  and empower you to lead while removing the uncertainty and silos.  Partner with the experts who help make business and technology simple and effective
Call-to-action section encouraging visitors to learn more about the company's services and expertise
Services -- detail provided in the attached word document (please use)
Section providing an overview of the company's services, including digital transformation, strategy, change management, CRM, ERP, automation, AI, data / analytics, process optimization, carve-outs, integrations, scaling, risk mitigation, security and marketing.
Call-to-action section encouraging visitors to learn more about the company's expertise and how it can help their business and encouraging visitors to schedule a consultation or assessment.
Footer
Navigation menu
Contact information
LinkedIn link
The website should have a modern and professional design, with a focus on clear messaging and easy navigation. The color scheme will be clean and simple, with a mix of colors to convey trust, reliability, and innovation. The website will be optimized for search engines and mobile devices, ensuring that visitors can easily access the site from any device.

Target Market(s)

Companies who desire to grow their business, optimize their processes, maximize the output of human capital and profitablity.

Industry/Entity Type

Business Technology consulting

Coding

Coded - Design and coding required

Number of Pages Required

4 page

Font styles to use
Other font styles liked:
• designer should choose for professional audience

Requirements
Must have
• easy navigation, engaging flow, professional layout and colors that represent confidence, excellence and innovation in a world full of change.
Nice to have
• I would like to see you blend in the play on DELTA's (changes that we face in business and life), the different way we may look at things and the unique way we solve problems. All of these are options to Walk UP bolder and leverage the unique views of individuals, millions of data points, workflow and technology enablers to deliver maximize value to your enterprise

```html
<!DOCTYPE html>
<html lang="en">
<head>
<meta charset="utf-8">
<title>Brimquarta — Business Technology Consulting</title>
<link href="https://fonts.googleapis.com/css2?family=Lexend:wght@400;500;600;700;800&family=Inter:wght@400;500;600&display=swap" rel="stylesheet">
<style>
:root{
  --blue:#1f8fe0;
  --blue-dark:#00518a;
  --navy:#0a1c2b;
  --ink:#111820;
  --text:#4d5560;
  --muted:#9aa2ab;
  --panel:#f2f3f5;
  --white:#ffffff;
}
*{margin:0;padding:0;box-sizing:border-box}
html,body{width:1200px;height:4623px;overflow:hidden}
body{position:relative;background:var(--white);font-family:'Inter',sans-serif;color:var(--text)}
.abs{position:absolute}
.head{font-family:'Lexend',sans-serif;color:var(--ink)}
.eyebrow{font-family:'Lexend',sans-serif;font-size:15px;letter-spacing:4px;color:var(--blue);font-weight:500;text-transform:uppercase}
.btn{position:absolute;background:var(--blue);color:#fff;border-radius:20px;font-family:'Lexend',sans-serif;font-weight:600;font-size:12px;letter-spacing:1px;display:flex;align-items:center;justify-content:center;text-transform:uppercase}

/* header */
.site-header{position:absolute;left:0;top:0;width:1200px;height:84px;background:#fff}
.brand{position:absolute;display:flex;align-items:center;gap:10px;font-family:'Lexend',sans-serif;font-weight:600;font-size:22px;color:var(--ink)}
.brand-mark{width:22px;height:22px;background:var(--blue)}
.nav a{position:absolute;top:34px;font-size:13px;color:#333;text-decoration:none}
.header-rule{position:absolute;left:540px;top:81px;width:536px;height:3px;background:var(--blue)}

/* hero */
.hero{position:absolute;left:0;top:84px;width:1200px;height:600px;background:linear-gradient(90deg,#05121d 0%,#0b2233 45%,#1d3340 70%,#3a3a36 100%);overflow:hidden}
.hero-photo{position:absolute;left:520px;top:0;width:680px;height:560px;background:radial-gradient(ellipse at 70% 40%,rgba(150,120,90,.55),rgba(20,40,55,0) 70%)}
.hero h1{position:absolute;left:124px;top:192px;font-family:'Lexend',sans-serif;font-weight:700;font-size:58px;line-height:75px;color:#fff;letter-spacing:2px}
.hero .eyebrow{position:absolute;left:124px;top:160px;font-size:13px}
.hero p{position:absolute;left:124px;top:362px;font-size:12px;color:#fff}

/* about */
.about-visual{position:absolute;left:81px;top:727px;width:502px;height:390px}
.about-copy{position:absolute;left:617px;top:688px;width:390px}
.about-copy h2{font-family:'Lexend',sans-serif;font-weight:600;font-size:29px;line-height:39px;color:var(--ink);margin-top:12px}
.about-copy p{font-size:12.5px;line-height:21.5px;color:var(--text);margin-top:36px}
.vision{margin-top:30px;width:383px;background:var(--panel);border-radius:12px;padding:14px 19px 16px}
.vision h4{font-size:12px;color:var(--blue);font-weight:500;margin-bottom:8px}
.vision p{margin:0;font-size:12.5px;line-height:21.5px}

/* services */
.section-title{position:absolute;left:0;width:1200px;text-align:center}
.section-title h2{font-family:'Lexend',sans-serif;font-weight:500;font-size:32px;line-height:43px;color:var(--ink);margin-top:8px}
.section-title .sub{font-size:17px;line-height:29px;color:#333;margin-top:12px}
.service-card{position:absolute;width:300px;height:298px;background:#fff;border-radius:14px;box-shadow:0 8px 30px rgba(0,40,80,.10);padding:36px 24px 0}
.service-card svg.icon{width:58px;height:52px}
.service-card h3{font-family:'Lexend',sans-serif;font-weight:600;font-size:16px;line-height:24px;letter-spacing:1.2px;color:var(--ink);position:absolute;left:24px;right:20px}
.service-card h3.caps{text-transform:uppercase;font-size:15px;line-height:26px}
.service-card p{position:absolute;left:24px;right:30px;font-size:12.5px;line-height:21.5px;color:var(--text)}
.service-card .go{position:absolute;right:38px;bottom:30px;width:14px;height:14px}

/* steps */
.step{position:absolute;width:220px;text-align:center}
.step h4{font-family:'Lexend',sans-serif;font-weight:600;font-size:17px;line-height:21px;color:var(--ink)}
.step p{font-size:12.5px;line-height:21.5px;color:var(--text);margin-top:10px}

/* solutions */
.pillar{position:absolute;width:250px}
.pillar h4{font-family:'Lexend',sans-serif;font-weight:500;font-size:17px;line-height:22px;letter-spacing:2px;color:#222;text-transform:uppercase}
.pillar p{font-size:12.5px;line-height:19px;color:var(--text)}
.pillar-icon{position:absolute;width:58px;height:58px;border-radius:50%;background:var(--blue);display:flex;align-items:center;justify-content:center}

/* reviews */
.review{position:absolute;width:304px;height:252px;background:#fff;border-radius:14px;box-shadow:0 8px 30px rgba(0,40,80,.10);text-align:center;padding:36px 34px 0}
.review.faded{opacity:.45}
.stars{color:#f2b441;font-size:16px;letter-spacing:3px}
.review q{display:block;font-size:12.5px;line-height:21.5px;color:#333;margin-top:16px;quotes:none}
.review .name{font-family:'Lexend',sans-serif;font-size:16px;color:var(--ink);margin-top:18px}
.review .role{font-size:11px;color:var(--muted);margin-top:4px}
.arrow-btn{position:absolute;width:50px;height:50px;border-radius:50%;background:#fff;box-shadow:0 4px 16px rgba(0,40,80,.15);display:flex;align-items:center;justify-content:center}

/* cta */
.cta h2{position:absolute;left:172px;top:3862px;font-family:'Lexend',sans-serif;font-weight:600;font-size:40px;line-height:54px;color:var(--ink)}
.cta h2 span{color:var(--blue)}

/* footer */
.site-footer{position:absolute;left:0;top:4200px;width:1200px;height:423px;background:var(--navy);color:#c9d2da}
.site-footer h5{position:absolute;font-family:'Lexend',sans-serif;font-weight:500;font-size:16px;color:#fff}
.site-footer ul{position:absolute;list-style:none;font-size:12.5px;line-height:29px}
.site-footer .legal{position:absolute;left:124px;top:197px;width:270px;font-size:10.5px;line-height:17.5px;color:#aab4bd}
.site-footer .rule{position:absolute;left:124px;top:342px;width:942px;height:1px;background:#33485a}
.social{position:absolute;top:376px;width:16px;height:16px;border-radius:50%;border:1.5px solid #c9d2da}
.copyright{position:absolute;right:134px;top:376px;font-size:12px;color:#fff}
</style>
</head>
<body>

<header class="site-header">
  <div class="brand" style="left:124px;top:26px"><span class="brand-mark"></span>Brimquarta</div>
  <nav class="nav">
    <a style="left:483px">Home</a>
    <a style="left:569px">About Us</a>
    <a style="left:673px">Services</a>
    <a style="left:777px">Testimonials</a>
  </nav>
  <div class="btn" style="left:908px;top:25px;width:168px;height:38px">Contact Us</div>
  <div class="header-rule"></div>
</header>

<section class="hero">
  <div class="hero-photo" role="img" aria-label="Photo of a developer working at a desk with several code monitors"></div>
  <div class="eyebrow">Brimquarta</div>
  <h1>WALKING UP<br>BOLDER</h1>
  <p>Life is full of delta “small shifts” and we approach each challenge uniquely.</p>
  <div class="btn" style="left:122px;top:416px;width:170px;height:38px">Get Started</div>
</section>
<svg class="abs" style="left:0;top:500px" width="1200" height="190" viewBox="0 0 1200 190">
  <path d="M0 40 C200 130 420 178 640 155 C860 130 1050 60 1200 40 L1200 190 L0 190Z" fill="#1f8fe0"/>
  <path d="M0 85 C220 160 430 185 640 172 C860 156 1050 95 1200 58 L1200 190 L0 190Z" fill="#fff"/>
</svg>

<section>
  <svg class="about-visual" viewBox="0 0 502 390" role="img" aria-label="Photo of a woman at a computer framed inside a triangle">
    <defs>
      <radialGradient id="haze" cx="50%" cy="45%" r="55%"><stop offset="0" stop-color="#e6e6e6"/><stop offset="1" stop-color="#fff" stop-opacity="0"/></radialGradient>
      <linearGradient id="tri" x1="0" y1="0" x2="0" y2="1"><stop offset="0" stop-color="#3a3f45"/><stop offset=".6" stop-color="#1e2a33"/><stop offset="1" stop-color="#0e1216"/></linearGradient>
    </defs>
    <ellipse cx="250" cy="190" rx="250" ry="165" fill="url(#haze)"/>
    <path d="M176 4 Q184 -6 192 4 L369 375 Q373 388 360 388 L0 388 Q-12 388 -6 375Z" transform="translate(48 0)" fill="url(#tri)"/>
  </svg>
  <div class="about-copy">
    <div class="eyebrow">About Us</div>
    <h2>Navigating Business<br>Deltas with Brimquarta's<br>Innovative Expertise</h2>
    <p>Brimquarta is not your typical business technology consulting firm. We specialize in innovation, simplification, and creative solutions. Whether you're a startup or a global conglomerate, we elevate your enterprise through digital transformation. From strategy to implementation, our focus is on optimizing, innovating, and aligning your business for success.</p>
    <div class="vision">
      <h4>Our Vision</h4>
      <p>Brimquarta is not your typical business technology consulting firm. We specialize in innovation, simplification, and creative solutions.</p>
    </div>
  </div>
</section>

<section>
  <svg class="abs" style="left:0;top:1238px" width="1200" height="760" viewBox="0 0 1200 760">
    <path d="M1200 0 C1120 95 1000 150 860 175 C770 192 730 220 730 300 L730 690 C900 710 1080 690 1200 600Z" fill="#00518a"/>
  </svg>
  <div class="section-title" style="top:1230px">
    <div class="eyebrow">Services</div>
    <h2>Our services cover a spectrum of<br>business technology needs</h2>
  </div>

  <div class="service-card" style="left:124px;top:1389px">
    <svg class="icon" viewBox="0 0 58 52" fill="none" stroke="#1f8fe0" stroke-width="2"><rect x="2" y="4" width="50" height="40" rx="3"/><path d="M2 12h50M8 20h14M8 26h14M8 32h14"/><circle cx="38" cy="30" r="8"/><circle cx="38" cy="30" r="3"/></svg>
    <h3 style="top:110px">SaaS CRM (Loyalty &amp; Subscription) Apps / Segmentation / Rewards</h3>
    <p style="top:192px">Embrace the future with our advanced digital solutions.</p>
    <svg class="go" viewBox="0 0 14 14" stroke="#1f8fe0" stroke-width="2" fill="none"><path d="M3 11L11 3M5 3h6v6"/></svg>
  </div>
  <div class="service-card" style="left:449px;top:1389px">
    <svg class="icon" viewBox="0 0 58 52" fill="none" stroke="#1f8fe0" stroke-width="2"><path d="M4 2h26l8 8v36H4z"/><path d="M10 34l8-10 6 6 6-10"/><circle cx="36" cy="36" r="8"/><path d="M42 42l8 8"/></svg>
    <h3 style="top:110px">Strategy / Org Design / Competitive Analysis / Change Management</h3>
    <p style="top:192px">Embrace the future with our advanced digital solutions.</p>
    <svg class="go" viewBox="0 0 14 14" stroke="#1f8fe0" stroke-width="2" fill="none"><path d="M3 11L11 3M5 3h6v6"/></svg>
  </div>
  <div class="service-card" style="left:775px;top:1389px">
    <svg class="icon" viewBox="0 0 58 52" fill="none" stroke="#1f8fe0" stroke-width="2"><circle cx="28" cy="16" r="10"/><circle cx="28" cy="16" r="4"/><circle cx="14" cy="34" r="8"/><circle cx="42" cy="34" r="8"/><path d="M28 26v20M14 42v6M42 42v6"/></svg>
    <h3 style="top:110px">M&amp;A - (Carve-outs / Integrations) Diligence / TSA / IMO / Interim CxO</h3>
    <p style="top:192px">Embrace the future with our advanced digital solutions.</p>
    <svg class="go" viewBox="0 0 14 14" stroke="#1f8fe0" stroke-width="2" fill="none"><path d="M3 11L11 3M5 3h6v6"/></svg>
  </div>

  <div class="service-card" style="left:124px;top:1713px">
    <svg class="icon" viewBox="0 0 58 52" fill="none" stroke="#1f8fe0" stroke-width="2"><rect x="4" y="2" width="30" height="44" rx="3"/><rect x="20" y="20" width="30" height="26" rx="3"/><path d="M10 10h16M10 16h8M28 30l-4 4 4 4M42 30l4 4-4 4"/></svg>
    <h3 class="caps" style="top:102px">Digital Transformation, App Dev, Social/Omni-Channel Solutions</h3>
    <p style="top:192px">Embrace the future with our advanced digital solutions.</p>
    <svg class="go" viewBox="0 0 14 14" stroke="#1f8fe0" stroke-width="2" fill="none"><path d="M3 11L11 3M5 3h6v6"/></svg>
  </div>
  <div class="service-card" style="left:449px;top:1713px">
    <svg class="icon" viewBox="0 0 58 52" fill="none" stroke="#1f8fe0" stroke-width="2"><circle cx="30" cy="14" r="10"/><circle cx="30" cy="14" r="4"/><path d="M4 36l10-4h14l-10 6h16l12-8 4 4-16 14H4z"/></svg>
    <h3 class="caps" style="top:102px">Process Optimization - Secure, Scalable, Compliant Systems</h3>
    <p style="top:192px">Embrace the future with our advanced digital solutions.</p>
    <svg class="go" viewBox="0 0 14 14" stroke="#1f8fe0" stroke-width="2" fill="none"><path d="M3 11L11 3M5 3h6v6"/></svg>
  </div>
  <div class="service-card" style="left:775px;top:1713px">
    <svg class="icon" viewBox="0 0 58 52" fill="none" stroke="#1f8fe0" stroke-width="2"><path d="M22 4c-10 0-16 8-14 18l-4 8h6v10h10v8"/><rect x="24" y="14" width="18" height="18" rx="2"/><path d="M28 14V8M38 14V8M28 32v6M38 32v6M42 20h6M42 26h6"/></svg>
    <h3 class="caps" style="top:102px">AI / Analytics / Automation</h3>
    <p style="top:168px">Embrace the future with our advanced digital solutions.</p>
    <svg class="go" viewBox="0 0 14 14" stroke="#1f8fe0" stroke-width="2" fill="none"><path d="M3 11L11 3M5 3h6v6"/></svg>
  </div>
</section>

<section>
  <div class="eyebrow abs" style="left:124px;top:2152px">How It Works</div>
  <div class="head abs" style="left:124px;top:2182px;font-size:32px;font-weight:500">Navigating Success</div>
  <svg class="abs" style="left:0;top:2220px" width="1200" height="260" viewBox="0 0 1200 260">
    <defs>
      <linearGradient id="flow" x1="0" y1="0" x2="0" y2="1"><stop offset="0" stop-color="#d7eaf8"/><stop offset="1" stop-color="#fff" stop-opacity="0"/></linearGradient>
    </defs>
    <path d="M122 51 C200 80 280 96 348 94 C440 90 500 50 592 57 C680 64 760 82 834 71 C930 56 1000 30 1089 28 L1089 256 L122 256Z" fill="url(#flow)"/>
    <path d="M122 51 C200 80 280 96 348 94 C440 90 500 50 592 57 C680 64 760 82 834 71 C930 56 1000 30 1089 28" fill="none" stroke="#1f8fe0" stroke-width="1.6" stroke-dasharray="3 4"/>
    <g stroke="#cfd9e2" stroke-width="1"><path d="M122 51V256M348 94V256M592 57V256M834 71V256M1089 28V256"/></g>
    <g fill="#fff" stroke="#1f8fe0" stroke-width="3"><circle cx="122" cy="51" r="8"/><circle cx="348" cy="94" r="8"/><circle cx="592" cy="57" r="8"/><circle cx="834" cy="71" r="8"/><circle cx="1089" cy="28" r="8"/></g>
  </svg>
  <div class="step" style="left:125px;top:2357px"><h4>Navigating<br>Success</h4><p>Dive into your business goals and challenges through joint discovery sessions.</p></div>
  <div class="step" style="left:360px;top:2320px"><h4>Tailored<br>Strategy</h4><p>Craft a personalized roadmap aligned with your unique objectives.</p></div>
  <div class="step" style="left:602px;top:2357px"><h4>Seamless<br>Execution</h4><p>Implement with excellence, leveraging innovative technologies.</p></div>
  <div class="step" style="left:844px;top:2321px"><h4>Continuous<br>Refinement</h4><p>Adapt and optimize continually for sustained success.</p></div>
</section>

<section>
  <div class="section-title" style="top:2600px">
    <div class="eyebrow">Solutions</div>
    <h2 style="font-weight:600">Empowering Your Business</h2>
    <div class="sub">Tailored Excellence: Elevating Your Business Through<br>Custom Solutions</div>
  </div>
  <svg class="abs" style="left:0;top:2800px" width="1200" height="320" viewBox="0 0 1200 320">
    <g fill="none" stroke="#8ec4ec" stroke-width="1.4" stroke-dasharray="5 4">
      <path d="M250 60H400L478 115"/><path d="M400 240H410L478 165"/>
      <path d="M950 60H800L720 115"/><path d="M950 240H790L720 165"/>
    </g>
    <circle cx="599" cy="135" r="117" fill="#e8f3fc"/>
    <circle cx="599" cy="135" r="108" fill="none" stroke="#bcdcf4" stroke-width="3"/>
    <circle cx="599" cy="135" r="98" fill="#1f8fe0"/>
    <g fill="#fff" stroke="#8ec4ec" stroke-width="2"><circle cx="478" cy="117" r="6"/><circle cx="478" cy="160" r="6"/><circle cx="720" cy="117" r="6"/><circle cx="720" cy="160" r="6"/></g>
  </svg>

  <div class="pillar-icon" style="left:158px;top:2800px"><svg width="28" height="28" viewBox="0 0 28 28" fill="none" stroke="#fff" stroke-width="2"><circle cx="14" cy="8" r="5"/><path d="M2 22l6-4h8l6-4 4 2-10 10H2z"/></svg></div>
  <div class="pillar" style="left:230px;top:2808px"><h4>Strategic<br>Alignment</h4></div>
  <div class="pillar" style="left:158px;top:2868px;width:255px"><p>Tailor-made strategies that align seamlessly with your business goals, ensuring a roadmap for success.</p></div>

  <div class="pillar-icon" style="left:158px;top:2982px"><svg width="28" height="28" viewBox="0 0 28 28" fill="none" stroke="#fff" stroke-width="2"><circle cx="14" cy="14" r="6"/><path d="M14 2v5M14 21v5M2 14h5M21 14h5M5 5l3 3M20 20l3 3M23 5l-3 3M8 20l-3 3"/></svg></div>
  <div class="pillar" style="left:230px;top:2990px"><h4>Tech<br>Innovation</h4></div>
  <div class="pillar" style="left:158px;top:3050px;width:255px"><p>Cutting-edge technologies and solutions designed to elevate your business in a rapidly evolving digital landscape.</p></div>

  <div class="pillar-icon" style="left:967px;top:2800px"><svg width="28" height="28" viewBox="0 0 28 28" fill="none" stroke="#fff" stroke-width="2"><rect x="4" y="4" width="16" height="14" rx="2"/><circle cx="18" cy="18" r="5"/><path d="M22 22l4 4"/></svg></div>
  <div class="pillar" style="left:793px;top:2808px"><h4>Operational<br>Excellence</h4></div>
  <div class="pillar" style="left:793px;top:2868px;width:240px"><p>Streamlined processes and optimizations that enhance efficiency, delivering tangible results for your bottom line.</p></div>

  <div class="pillar-icon" style="left:967px;top:2982px"><svg width="28" height="28" viewBox="0 0 28 28" fill="none" stroke="#fff" stroke-width="2"><path d="M14 2v24M14 6h8l3 3-3 3h-8M14 14H6l-3 3 3 3h8"/></svg></div>
  <div class="pillar" style="left:793px;top:2990px"><h4>Personalized<br>Guidance</h4></div>
  <div class="pillar" style="left:793px;top:3050px;width:240px"><p>Dedicated experts working closely with you, providing personalized guidance and support throughout your business transformation journey.</p></div>

  <div class="btn" style="left:515px;top:3152px;width:169px;height:38px">Contact Us</div>
</section>

<section>
  <div class="abs" style="left:0;top:3230px;width:1200px;height:290px;background:linear-gradient(180deg,#fff,#f1f7fd)"></div>
  <div class="section-title" style="top:3290px">
    <div class="eyebrow">Reviews</div>
    <h2 style="font-weight:600">Client Testimonials</h2>
    <div class="sub">Clients Speak on Their Transformative Brimquarta<br>Experience</div>
  </div>

  <div class="review faded" style="left:-198px;top:3480px;padding-left:34px;text-align:right"><q>"Theirs are top-notch and our most sensitive needs haven't…</q></div>
  <div class="review faded" style="left:124px;top:3480px"><div class="stars">★★★★★</div><q>"Partnering with Brimquarta was a game-changer for our business. Their personalized approach and deep understanding of our goals allowed th…</q><div class="name">Mara Ellison</div><div class="role">Defence Analyst</div></div>
  <div class="review" style="left:447px;top:3480px"><div class="stars">★★★★★</div><q>"Partnering with Brimquarta was a game-changer for our business. Their personalized approach and deep understanding of our goals allowed th…</q><div class="name">Tobin Reyes</div><div class="role">NCA Manager</div></div>
  <div class="review faded" style="left:771px;top:3480px"><div class="stars">★★★★★</div><q>"Partnering with Brimquarta was a game-changer for our business. Their personalized approach and deep understanding of our goals allowed th…</q><div class="name">Idris Calloway</div><div class="role">Chief Information Officer</div></div>
  <div class="review faded" style="left:1094px;top:3480px;text-align:left"><q>"Their cyber notch. We sensitive…</q></div>

  <div class="arrow-btn" style="left:95px;top:3579px"><svg width="18" height="18" viewBox="0 0 18 18" fill="none" stroke="#1f8fe0" stroke-width="2"><path d="M15 9H3M8 4L3 9l5 5"/></svg></div>
  <div class="arrow-btn" style="left:1051px;top:3572px"><svg width="18" height="18" viewBox="0 0 18 18" fill="none" stroke="#1f8fe0" stroke-width="2"><path d="M3 9h12M10 4l5 5-5 5"/></svg></div>
</section>

<section class="cta">
  <div class="abs" role="img" aria-label="Soft flowing blue wave lines background" style="left:0;top:3760px;width:1200px;height:400px;background:radial-gradient(ellipse at 75% 45%,#e3f0fb 0%,rgba(255,255,255,0) 60%),linear-gradient(180deg,#fff,#eef6fd)"></div>
  <h2><span>DISCOVER</span> HOW OUR EXPERTISE<br>CAN DRIVE <span>YOUR BUSINESS</span><br>TOWARDS SUCCESS.</h2>
  <div class="btn" style="left:181px;top:4055px;width:169px;height:38px">Get Started</div>
</section>
<svg class="abs" style="left:0;top:4100px" width="1200" height="110" viewBox="0 0 1200 110">
  <path d="M0 10 C200 60 380 95 600 92 C820 88 1020 40 1200 8 L1200 110 L0 110Z" fill="#1f8fe0"/>
  <path d="M0 40 C220 90 400 105 600 104 C820 102 1020 65 1200 30 L1200 110 L0 110Z" fill="#0a1c2b"/>
</svg>

<footer class="site-footer">
  <div class="brand" style="left:124px;top:110px;color:#fff"><span class="brand-mark"></span>Brimquarta</div>
  <p class="legal">Brimquarta is a private company and is not affiliated with or endorsed by the Northgate Civic Authority. Any references to NCA are for informational purposes only.</p>

  <h5 style="left:475px;top:110px">Quick Links</h5>
  <ul style="left:475px;top:155px"><li>Home</li><li>About</li><li>Services</li><li>Contact Us</li><li>Testimonials</li></ul>

  <h5 style="left:676px;top:110px">Help</h5>
  <ul style="left:676px;top:155px"><li>FAQs</li><li>Support</li><li>Get Started Guide</li><li>Contact Support</li></ul>

  <h5 style="left:854px;top:110px">Contact Information</h5>
  <ul style="left:854px;top:155px">
    <li><svg width="12" height="12" viewBox="0 0 12 12" fill="#1f8fe0" style="margin-right:8px;vertical-align:-1px"><path d="M6 0a4 4 0 0 1 4 4c0 3-4 8-4 8S2 7 2 4a4 4 0 0 1 4-4zm0 2.5a1.5 1.5 0 1 0 0 3 1.5 1.5 0 0 0 0-3z"/></svg>48 Larkspur Row, Fenwick Bay</li>
    <li><svg width="12" height="12" viewBox="0 0 12 12" fill="#1f8fe0" style="margin-right:8px;vertical-align:-1px"><path d="M2 0l3 3-1.5 2a7 7 0 0 0 3.5 3.5L9 7l3 3-2 2C5 12 0 7 0 2z"/></svg>+1 (555) 010-7731</li>
    <li><svg width="12" height="12" viewBox="0 0 12 12" fill="none" stroke="#1f8fe0" stroke-width="1.5" style="margin-right:8px;vertical-align:-1px"><rect x="1" y="2" width="10" height="8"/><path d="M1 2l5 4 5-4"/></svg>info@brimquarta.example</li>
  </ul>

  <div class="rule"></div>
  <span class="social" style="left:124px"></span>
  <span class="social" style="left:158px"></span>
  <span class="social" style="left:192px"></span>
  <span class="social" style="left:226px"></span>
  <span class="social" style="left:260px"></span>
  <div class="copyright">© 2023 Brimquarta. All Rights Reserved.&nbsp; Privacy Policy | Terms Of Service</div>
</footer>

</body>
</html>
```